Parkinson's Disease Progression

Visually describe the rate of Parkinson progression in the first 15 years following diagnosis. Title: "Patient-Perceived Progression of Parkinsonism"

The attached figure names "meanqol" is the curve that should serve as the basis of this graphic. Everything else-- color, labels, font, etc. describe this curve.
Thank you!

Target Market(s)

People with Parkisnon's Disease, neurologists, family members.

Font styles to use
Sans Serif

Requirements
Must have
• Must have the lines going through these exact numbers
Excellent -- 502
Very good- 661
Good- 895
Fair- 1268
Poor- 1655

LABELS:
Title: "Patient-Perceived Progression of Parkinsonism"
"SWI-TC (Self-Logged Wellbeing Index for Tremor Conditions)" should be the label on the left.
"Quality of Life" should be the label on the right
"Years Since Diagnosis" should be the label on the bottom
Nice to have
• A color scheme that goes from GOOD (low numbers) to BAD (high numbers).

Easy to read (elderly)

```html
<!DOCTYPE html>
<html lang="en">
<head>
<meta charset="utf-8">
<title>Patient-Perceived Progression of Parkinsonism</title>
<link href="https://fonts.googleapis.com/css2?family=Source+Serif+4:ital,wght@0,400;0,600;0,700;1,400&family=Source+Sans+3:ital,wght@0,400;0,600;1,400;1,600&display=swap" rel="stylesheet">
<style>
  :root {
    --page: #f4f4f4;
    --panel: #e9e9eb;
    --ink: #111111;
    --accent: #b81c2d;
    --excellent: #6f9e40;
    --very-good: #86bf4e;
    --good: #c8da86;
    --fair: #ee7c5d;
    --poor: #b81c2d;
    --grid: #d6d6d8;
    --serif: "Source Serif 4", Georgia, serif;
    --sans: "Source Sans 3", Arial, sans-serif;
  }
  * { margin: 0; padding: 0; box-sizing: border-box; }
  html, body { width: 1200px; height: 993px; overflow: hidden; background: var(--page); }
  .poster {
    position: absolute; left: 0; top: 36px;
    width: 1356px; height: 1040px;
    transform: scale(0.885); transform-origin: 0 0;
    background: var(--page); color: var(--ink);
    font-family: var(--sans);
  }
  .title-panel {
    position: absolute; left: 32px; top: 26px; width: 747px; height: 435px;
    background: var(--panel);
  }
  .title {
    position: absolute; left: 27px; top: 22px;
    font-family: var(--serif); font-weight: 700; font-size: 46px; line-height: 49px;
  }
  .year {
    position: absolute; right: 30px; top: 26px;
    font-family: var(--serif); font-weight: 700; font-size: 36px; color: var(--accent);
    border-left: 5px solid var(--ink); padding-left: 18px; line-height: 40px;
  }
  .authors {
    position: absolute; right: 27px; top: 288px;
    font-style: italic; font-weight: 600; font-size: 20px;
  }
  .link-block { position: absolute; top: 340px; }
  .link-block.details { left: 27px; }
  .link-block.participate { right: 23px; text-align: right; }
  .link-label { color: var(--accent); font-style: italic; font-weight: 600; font-size: 16px; }
  .link-url { font-family: var(--serif); font-weight: 600; font-size: 17px; }
  .bar-panel {
    position: absolute; left: 800px; top: 26px; width: 525px; height: 435px;
    background: var(--panel);
  }
  .graphics { position: absolute; left: 0; top: 0; }
</style>
</head>
<body>
<main class="poster">
  <section class="title-panel">
    <h1 class="title">Patient-<br>Perceived Progression<br>of Parkinsonism</h1>
    <div class="year">2020</div>
    <p class="authors">RJ Halvorsen et al.</p>
    <div class="link-block details">
      <p class="link-label">For study details:</p>
      <p class="link-url">www.SteadyDaysStudy.org</p>
    </div>
    <div class="link-block participate">
      <p class="link-label">To participate in this study:</p>
      <p class="link-url">www.WellbeingTremorStudy.edu</p>
    </div>
  </section>

  <section class="bar-panel"></section>

  <svg class="graphics" width="1356" height="1040" viewBox="0 0 1356 1040" font-family="Source Sans 3, Arial, sans-serif">
    <!-- Bar chart: score by quality-of-life rating -->
    <g class="bar-chart">
      <text x="1080" y="72" text-anchor="middle" font-family="Source Serif 4, Georgia, serif" font-weight="700" font-size="22">In General, Would You Say Your</text>
      <text x="1080" y="99" text-anchor="middle" font-family="Source Serif 4, Georgia, serif" font-weight="700" font-size="22">Quality of Life is:</text>
      <g stroke="var(--grid)" stroke-width="1">
        <line x1="899" y1="126" x2="1299" y2="126"/>
        <line x1="899" y1="194" x2="1299" y2="194"/>
        <line x1="899" y1="263" x2="1299" y2="263"/>
        <line x1="899" y1="331" x2="1299" y2="331"/>
        <line x1="899" y1="399" x2="1299" y2="399"/>
      </g>
      <g font-size="17" text-anchor="end">
        <text x="887" y="132">2000</text>
        <text x="887" y="200">1500</text>
        <text x="887" y="269">1000</text>
        <text x="887" y="337">500</text>
        <text x="887" y="405">0</text>
      </g>
      <text transform="translate(830 246) rotate(-90)" text-anchor="middle" font-style="italic" font-weight="600" font-size="16">SWI-TC</text>
      <rect x="916" y="330.5" width="56" height="68.5" fill="var(--excellent)"/>
      <rect x="994" y="308.8" width="56" height="90.2" fill="var(--very-good)"/>
      <rect x="1072" y="276.8" width="56" height="122.2" fill="var(--good)"/>
      <rect x="1150" y="225.9" width="56" height="173.1" fill="var(--fair)"/>
      <rect x="1228" y="173.1" width="56" height="225.9" fill="var(--poor)"/>
      <g font-size="18" text-anchor="middle">
        <text x="944" y="312">502</text>
        <text x="1022" y="296">661</text>
        <text x="1100" y="281">895</text>
        <text x="1178" y="234">1268</text>
        <text x="1256" y="173">1655</text>
      </g>
      <g font-size="16" text-anchor="middle">
        <text x="944" y="434">Excellent</text>
        <text x="1022" y="434">Very Good</text>
        <text x="1100" y="434">Good</text>
        <text x="1178" y="434">Fair</text>
        <text x="1256" y="434">Poor</text>
      </g>
    </g>

    <!-- Progression chart -->
    <g class="progression-chart">
      <rect x="32" y="482" width="99" height="458" fill="var(--ink)"/>
      <text transform="translate(74 711) rotate(-90)" text-anchor="middle" fill="#fff" font-style="italic" font-size="26">SWI-TC (Self-Logged Wellbeing</text>
      <text transform="translate(107 711) rotate(-90)" text-anchor="middle" fill="#fff" font-style="italic" font-size="26">Index for Tremor Conditions)</text>

      <rect x="1266" y="482" width="59" height="458" fill="var(--ink)"/>
      <text transform="translate(1304 700) rotate(-90)" text-anchor="middle" fill="#fff" font-style="italic" font-size="26">Quality Of Life</text>

      <rect x="243" y="482" width="1016" height="28" fill="var(--poor)"/>
      <rect x="243" y="510" width="1016" height="133" fill="var(--fair)"/>
      <rect x="243" y="643" width="1016" height="83" fill="var(--good)"/>
      <rect x="243" y="726" width="1016" height="56" fill="var(--very-good)"/>
      <rect x="243" y="782" width="1016" height="158" fill="var(--excellent)"/>
      <line x1="982" y1="482" x2="982" y2="940" stroke="#fff" stroke-width="3"/>

      <g font-size="24" text-anchor="end">
        <text x="1235" y="505" fill="#fff">Poor</text>
        <text x="1235" y="582">Fair</text>
        <text x="1235" y="688">Good</text>
        <text x="1235" y="765">Very Good</text>
        <text x="1235" y="868">Excellent</text>
      </g>

      <g stroke-width="5">
        <line x1="233" y1="607" x2="243" y2="607" stroke="var(--fair)"/>
        <line x1="233" y1="676" x2="243" y2="676" stroke="var(--good)"/>
        <line x1="233" y1="745" x2="243" y2="745" stroke="var(--very-good)"/>
        <line x1="233" y1="815" x2="243" y2="815" stroke="var(--excellent)"/>
        <line x1="233" y1="884" x2="243" y2="884" stroke="var(--excellent)"/>
      </g>
      <g font-size="24" text-anchor="end">
        <text x="205" y="615">1000</text>
        <text x="205" y="684">800</text>
        <text x="205" y="753">600</text>
        <text x="205" y="823">400</text>
        <text x="205" y="892">200</text>
      </g>

      <path d="M267 767 C320 752 380 715 479 693 C520 686 560 690 609 673 C650 660 690 625 779 590 C830 568 875 552 910 526
               L910 620 C880 612 830 612 779 614 C720 640 690 668 609 688 C560 706 520 705 479 709 C400 725 320 790 267 840 Z"
            fill="rgba(255,255,255,0.35)"/>
      <path d="M267 767 C320 752 380 715 479 693 C520 686 560 690 609 673 C650 660 690 625 779 590 C830 568 875 552 910 526"
            fill="none" stroke="var(--ink)" stroke-width="1.5" stroke-dasharray="4 3"/>
      <path d="M267 840 C320 790 400 725 479 709 C520 705 560 706 609 688 C690 668 720 640 779 614 C830 612 880 612 910 620"
            fill="none" stroke="var(--ink)" stroke-width="1.5" stroke-dasharray="4 3"/>
      <path d="M267 802 C320 775 380 735 479 701 C520 695 560 700 609 681 C650 668 690 638 779 602 C830 585 875 578 910 572"
            fill="none" stroke="var(--ink)" stroke-width="2.2"/>

      <g stroke="var(--excellent)" stroke-width="5">
        <line x1="266" y1="940" x2="266" y2="950"/>
        <line x1="481" y1="940" x2="481" y2="950"/>
        <line x1="696" y1="940" x2="696" y2="950"/>
        <line x1="910" y1="940" x2="910" y2="950"/>
      </g>
      <g font-size="24" text-anchor="middle">
        <text x="267" y="981">0</text>
        <text x="481" y="979">5</text>
        <text x="696" y="978">10</text>
        <text x="911" y="978">15</text>
      </g>
      <text x="625" y="1015" text-anchor="middle" font-style="italic" font-weight="600" font-size="26">Years Since Diagnosis</text>
      <g stroke="var(--ink)" stroke-width="2" fill="var(--ink)">
        <line x1="250" y1="1009" x2="487" y2="1009"/>
        <path d="M243 1009 L255 1004 L255 1014 Z" stroke="none"/>
        <line x1="775" y1="1009" x2="972" y2="1009"/>
        <path d="M979 1009 L967 1004 L967 1014 Z" stroke="none"/>
      </g>
    </g>
  </svg>
</main>
</body>
</html>
```